Financial Consulting Company in need of technical diagram

Attached is a basic template to follow, however the following changes must be made:
- Get rid of reflection boxes at the bottom
-Delete anything in parentheses
-Change top box to read "Uncover Value Opportunities"
-Change bottom right box to read "Sales and Operations Planning"
-Change bottom left box to read "Financial Planning"

Additionally we would like to see something a little more creative and cohesive. One possibility is using "Cheveron" type arrows to show the "wheel" effect.

Please email mtorvek@halbrine.example if you have any questions!
Updates

Please see newly uploaded image for an example of how we would like it re-created.

Project Deadline Extended

Industry/Entity Type

Financial

Requirements
Must have
• I'm looking for something that keeps the "wheel" approach, but is not a direct re-creation of the example given. The boxes for example, dont' necessarily need to stay boxes. Feel free to play around with placement as well.
Nice to have
• Please see green wheel for example of how it can be re-created.

```html
<!DOCTYPE html>
<html lang="en">
<head>
<meta charset="utf-8">
<title>Value Cycle Wheel</title>
<link rel="stylesheet" href="https://fonts.googleapis.com/css2?family=Roboto+Condensed:wght@700&display=swap">
<style>
  :root {
    --bg: #ffffff;
    --seg-orange: #efa052;
    --seg-red: #e6303f;
    --seg-magenta: #e0198c;
    --seg-navy: #333a8f;
    --seg-blue: #0c86c7;
    --seg-green: #00a56f;
    --seg-yellow: #f7e04a;
    --seam: #f4f4f4;
    --ink-dark: #111111;
    --ink-light: #ffffff;
  }
  html, body {
    margin: 0;
    padding: 0;
    width: 1200px;
    height: 1129px;
    overflow: hidden;
    background: var(--bg);
  }
  .wheel {
    display: block;
    width: 1200px;
    height: 1129px;
  }
  .segment {
    stroke: var(--seam);
    stroke-width: 4;
    stroke-linejoin: round;
  }
  .segment--orange { fill: var(--seg-orange); }
  .segment--red { fill: var(--seg-red); }
  .segment--magenta { fill: var(--seg-magenta); }
  .segment--navy { fill: var(--seg-navy); }
  .segment--blue { fill: var(--seg-blue); }
  .segment--green { fill: var(--seg-green); }
  .segment--yellow { fill: var(--seg-yellow); }
  .bevel {
    fill: none;
    stroke: rgba(255,255,255,0.28);
    stroke-width: 6;
  }
  .stage-label {
    font-family: "Roboto Condensed", "Arial Narrow", sans-serif;
    font-weight: 700;
    font-size: 46px;
    letter-spacing: -1.5px;
    text-anchor: middle;
    paint-order: stroke;
    stroke-linejoin: round;
  }
  .stage-label--compact { font-size: 42px; }
  .stage-label--dark {
    fill: var(--ink-dark);
    stroke: rgba(255,255,255,0.55);
    stroke-width: 3;
  }
  .stage-label--light {
    fill: var(--ink-light);
    stroke: rgba(0,0,0,0.7);
    stroke-width: 4;
  }
</style>
</head>
<body>
<svg class="wheel" viewBox="0 0 1200 1129" xmlns="http://www.w3.org/2000/svg" aria-label="Seven stage value cycle wheel">
  <defs>
    <path id="chevron-segment" d="M545,0 A545,545 0 0 1 339.8,426.1 L243.8,367.4 L210.1,263.5 A337,337 0 0 0 337,0 L439.3,38.4 Z"/>
    <filter id="wheel-shadow" x="-10%" y="-10%" width="120%" height="120%">
      <feDropShadow dx="3" dy="5" stdDeviation="5" flood-color="#000" flood-opacity="0.3"/>
    </filter>
  </defs>

  <g class="ring" filter="url(#wheel-shadow)" transform="translate(592,567)">
    <use href="#chevron-segment" class="segment segment--orange" transform="rotate(-115)"/>
    <use href="#chevron-segment" class="segment segment--red" transform="rotate(-63.57)"/>
    <use href="#chevron-segment" class="segment segment--magenta" transform="rotate(-12.14)"/>
    <use href="#chevron-segment" class="segment segment--navy" transform="rotate(39.29)"/>
    <use href="#chevron-segment" class="segment segment--blue" transform="rotate(90.71)"/>
    <use href="#chevron-segment" class="segment segment--green" transform="rotate(142.14)"/>
    <use href="#chevron-segment" class="segment segment--yellow" transform="rotate(193.57)"/>
    <circle class="bevel" r="540"/>
    <circle class="bevel" r="342"/>
  </g>

  <text class="stage-label stage-label--dark" transform="translate(600,128)">
    <tspan x="0" y="-20">Uncover Value</tspan>
    <tspan x="0" y="26">Opportunities</tspan>
  </text>

  <text class="stage-label stage-label--dark" transform="translate(944,312) rotate(60)">
    <tspan x="0" y="-8">Strategize</tspan>
    <tspan x="0" y="38">&amp; Align</tspan>
  </text>

  <text class="stage-label stage-label--light stage-label--compact" transform="translate(748,966) rotate(-24)">
    <tspan x="0" y="-6">Sales &amp; Operations</tspan>
    <tspan x="0" y="36">Planning</tspan>
  </text>

  <text class="stage-label stage-label--light stage-label--compact" transform="translate(372,935) rotate(31)">
    <tspan x="0" y="0">Financial Planning</tspan>
  </text>

  <text class="stage-label stage-label--dark" transform="translate(246,282) rotate(-57)">
    <tspan x="0" y="-8">Assess the</tspan>
    <tspan x="0" y="38">Results</tspan>
  </text>
</svg>
</body>
</html>
```